Business Card for TVK, logo files already created

Please, can you assist with creating a Business card the TVK graphics which are already listed on www.brinmoretech.example
The business card should be modern and upmarket, textured designs are welcome. Please feel free to express yourself and be very bold with your design.

Target Market(s)

Cyber Security

Industry/Entity Type

Information Technology

Contact Information for Business Card

Company Name
Name
Title
Mobile
Fax or Tel
email
url

Font styles to use
Serif
Sans Serif

Colors
3277b5
85acd3
ffffff

```html
<!DOCTYPE html>
<html lang="en">
<head>
<meta charset="utf-8">
<title>TVK Business Card</title>
<link href="https://fonts.googleapis.com/css2?family=Michroma&family=Open+Sans:wght@700&family=PT+Sans+Narrow&display=swap" rel="stylesheet">
<style>
  :root {
    --page-bg: #2ff3f6;
    --card-front: #9fe244;
    --card-back: #e4e4e6;
    --navy: #1f3a93;
    --ink: #1b2440;
    --accent-blue: #3277b5;
    --grey-text: #3a3a3a;
    --icon: #3b3f4a;
  }
  * { margin: 0; padding: 0; box-sizing: border-box; }
  html, body { width: 1200px; height: 1200px; overflow: hidden; }
  body { background: var(--page-bg); position: relative; }

  .card {
    position: absolute;
    left: 302px;
    width: 595px;
    height: 357px;
  }
  .card--front { top: 204px; background: var(--card-front); }
  .card--back { top: 638px; background: var(--card-back); }

  .brand {
    position: absolute;
    text-align: center;
    color: var(--navy);
    font-family: "Michroma", sans-serif;
    font-weight: 400;
    white-space: nowrap;
    transform: translateX(-50%);
  }
  .card--front .brand { left: 50%; top: 122px; }
  .brand__mark { font-size: 48px; line-height: 56px; letter-spacing: 3px; }
  .brand__name { font-size: 12px; line-height: 18px; margin-top: 6px; letter-spacing: 0.5px; }
  .brand__tagline { font-size: 9px; line-height: 14px; letter-spacing: 1px; margin-top: 4px; }

  .card--back .brand { left: 460px; top: 196px; }
  .card--back .brand__mark { font-size: 38px; line-height: 44px; letter-spacing: 2px; }
  .card--back .brand__name { font-size: 9.5px; line-height: 14px; margin-top: 5px; letter-spacing: 0.4px; }
  .card--back .brand__tagline { font-size: 7px; line-height: 11px; margin-top: 3px; letter-spacing: 0.8px; }

  .holder {
    position: absolute;
    left: 42px;
    top: 70px;
  }
  .holder__name {
    display: flex;
    align-items: center;
    gap: 4px;
    font-family: "Open Sans", sans-serif;
    font-weight: 700;
    font-size: 23px;
    line-height: 30px;
    color: var(--ink);
    letter-spacing: -0.3px;
  }
  .holder__name .surname { color: var(--accent-blue); }
  .holder__title {
    margin-left: 22px;
    font-family: "PT Sans Narrow", sans-serif;
    font-size: 17px;
    letter-spacing: 1px;
    color: var(--grey-text);
  }

  .contacts {
    position: absolute;
    left: 52px;
    top: 158px;
    list-style: none;
    font-family: "PT Sans Narrow", sans-serif;
    font-size: 18px;
    color: var(--ink);
  }
  .contacts li {
    position: absolute;
    left: 0;
    display: flex;
    align-items: center;
    gap: 6px;
    white-space: nowrap;
  }
  .contacts svg { width: 14px; height: 14px; flex: none; }
  .contacts .row-mobile { top: 0; }
  .contacts .row-phone { top: 35px; }
  .contacts .row-fax { top: 59px; }
  .contacts .row-mail { top: 88px; }
  .contacts .row-web { top: 111px; }
</style>
</head>
<body>

  <section class="card card--front">
    <div class="brand">
      <div class="brand__mark">TVK</div>
      <div class="brand__name">BRINMORE TECH SOLUTIONS</div>
      <div class="brand__tagline">SECURE BY DESIGN</div>
    </div>
  </section>

  <section class="card card--back">
    <div class="holder">
      <div class="holder__name">
        <svg width="18" height="22" viewBox="0 0 18 22" fill="none" stroke="#3b3f4a" stroke-width="1.3" aria-hidden="true">
          <circle cx="9" cy="7" r="4.5"/>
          <path d="M1.5 21 v-3 c0-3 3-5 7.5-5 s7.5 2 7.5 5 v3 z"/>
        </svg>
        <span>OWEN <span class="surname">HARTLEY</span></span>
      </div>
      <div class="holder__title">Designation</div>
    </div>

    <ul class="contacts">
      <li class="row-mobile">
        <svg viewBox="0 0 14 14" fill="none" stroke="#3b3f4a" stroke-width="1.1"><rect x="3.5" y="0.8" width="7" height="12.4" rx="1"/><line x1="6" y1="11" x2="8" y2="11"/></svg>
        014-555-0192
      </li>
      <li class="row-phone">
        <svg viewBox="0 0 14 14" fill="none" stroke="#3b3f4a" stroke-width="1.1"><path d="M3 1.5 l2 3 -1.3 1.3 c.8 1.8 2.2 3.2 4 4 l1.3-1.3 3 2 -1.5 2 c-5 -.5 -8.8-4.3-9.3-9.3z"/></svg>
        014-555-0192
      </li>
      <li class="row-fax">
        <svg viewBox="0 0 14 14" fill="none" stroke="#3b3f4a" stroke-width="1.1"><rect x="1" y="5" width="12" height="5.5" rx="1"/><rect x="3.5" y="1.5" width="7" height="3.5"/><rect x="3.5" y="8.5" width="7" height="4"/></svg>
        014-555-0192
      </li>
      <li class="row-mail">
        <svg viewBox="0 0 14 14" fill="none" stroke="#3b3f4a" stroke-width="1.1"><rect x="1" y="3" width="12" height="8.5"/><path d="M1 3 l6 5 6-5"/></svg>
        hello@brinmoretech.example
      </li>
      <li class="row-web">
        <svg viewBox="0 0 14 14" fill="none" stroke="#3b3f4a" stroke-width="1.1"><circle cx="7" cy="7" r="5.8"/><ellipse cx="7" cy="7" rx="2.6" ry="5.8"/><line x1="1.2" y1="7" x2="12.8" y2="7"/></svg>
        www.brinmoretech.example
      </li>
    </ul>

    <div class="brand">
      <div class="brand__mark">TVK</div>
      <div class="brand__name">BRINMORE TECH SOLUTIONS</div>
      <div class="brand__tagline">SECURE BY DESIGN</div>
    </div>
  </section>

</body>
</html>
```